Web design for community centre - bright colours (provided) and matching existing logo

Website based on a provided logo and existing website template skeleton (it is a Wordpress theme we must use that is already installed)

Basically, see if you can improve the existing theme skeleton at https://tarvoshub.org.au/redesign/. Mostly we are looking for a much nicer menu that works with the logo, and a nice font/design for text content.

We have a developer who will work your design into the Wordpress theme – so you can get creative in a graphic software app and our developer can most likely implement your ideas.

The website ideally will include design ideas from the logo (e.g. the idea of people with their arms around each other, colours).

Improvement to the text displayed on the photo slider (e.g. a colour border or other decoration) is also needed.

It needs a 'community' feel.

Target Market(s)

Parents (provides childcare), older people, people with disabilities, recent migrants

Industry/Entity Type

Community Center

Number of Pages Required

1 page

Font styles to use
Sans Serif

Colors

Designer to choose colors to be used in the design.

Requirements
Must have
• A very aesthetic top menu. Nice use of spacing, negative space etc.
• Fonts need to be legally available without a pageview fee (one off purchase OK). You need to provide proof we can use the font legally.
• See https://www.plover.org.au/ for an example of a menu we like.
• Must use the existing logo, provided in this brief.
• Needs to use colours from the logo but do not need to use all of them!
• Must be workable into the theme already installed at https://tarvoshub.org.au/redesign
Nice to have
• Maybe some kind of shapes attached to each menu link (top menu0
• A use of all 5 colours on the top menu, when you hover on it
Should not have
• Serif fonts

```html
<!DOCTYPE html>
<html lang="en">
<head>
<meta charset="utf-8">
<title>Tarvos Neighbourhood Learning Centre</title>
<link rel="stylesheet" href="https://fonts.googleapis.com/css2?family=Exo+2:wght@300;400;600;700&family=Roboto:wght@400;500&display=swap">
<style>
:root{
  --green:#8cc63f;
  --orange:#f7941d;
  --blue:#00aeef;
  --pink:#ec1c75;
  --purple:#662d91;
  --ink:#222;
  --body:#555;
  --panel:#f2f2f2;
  --line:#ccc;
  --s1:#3b5998;
  --s2:#3f729b;
  --s3:#55acee;
  --s4:#1ab7ea;
}
*{box-sizing:border-box;margin:0;padding:0}
html,body{width:989px;height:1200px;overflow:hidden;background:#fff}
body{position:relative;font-family:'Roboto',Arial,sans-serif;color:var(--ink)}

.brand{position:absolute;top:14px;left:0;width:989px;display:flex;justify-content:center;align-items:center;gap:10px}
.brand-dot{width:52px;height:52px;border-radius:50%;background:var(--blue)}
.brand-name{font-family:'Exo 2',Arial,sans-serif;font-weight:600;font-size:19px;line-height:21px;color:var(--ink);width:190px}

.main-nav{position:absolute;top:124px;left:46px;width:896px;display:flex;justify-content:space-between}
.main-nav a{font-size:13px;font-weight:500;color:#333;text-decoration:none;letter-spacing:.2px;padding-bottom:9px;border-bottom:2px solid}
.main-nav a.active{color:var(--green)}
.nav-green{border-color:var(--green)!important}
.nav-orange{border-color:var(--orange)!important}
.nav-blue{border-color:var(--blue)!important}
.nav-pink{border-color:var(--pink)!important}
.nav-purple{border-color:var(--purple)!important}

.hero{position:absolute;top:181px;left:46px;width:896px;height:347px;display:flex}
.hero-slide{position:relative;width:582px;height:347px;background:linear-gradient(135deg,#5a3a26 0%,#7a5236 35%,#b08366 55%,#6b4630 100%)}
.slide-arrow{position:absolute;top:165px}
.slide-arrow.prev{left:12px}
.slide-arrow.next{right:10px}
.slide-caption{position:absolute;left:0;bottom:0;width:582px;height:103px;background:rgba(40,28,22,.72);border-left:7px solid var(--green);padding:16px 30px 0 32px}
.slide-caption h2{font-family:'Exo 2',Arial,sans-serif;font-weight:400;font-size:25px;color:var(--green);line-height:28px}
.slide-caption p{font-size:13px;line-height:19px;color:#fff;margin-top:6px}

.newsletter{width:314px;height:347px;background:var(--panel);padding:52px 0 0 47px}
.newsletter h3{font-family:'Exo 2',Arial,sans-serif;font-weight:300;font-size:22px;line-height:26px;color:#111}
.newsletter h3 strong{font-weight:700;display:block}
.email-field{display:block;margin-top:24px;width:219px;height:35px;border:1px solid var(--line);background:#fff;font-size:11px;color:#777;padding:0 8px;line-height:33px}
.subscribe-btn{display:block;margin-top:14px;width:99px;height:32px;background:var(--orange);color:#fff;font-weight:500;font-size:13px;line-height:32px;text-align:center}
.social-row{display:flex;gap:6px;margin-top:35px}
.social-row span{width:38px;height:38px;display:block}
.sq1{background:var(--s1)}.sq2{background:var(--s2)}.sq3{background:var(--s3)}.sq4{background:var(--s4)}

.features{position:absolute;top:592px;left:47px;width:894px;display:flex;justify-content:space-between}
.feature{width:261px;text-align:center;border-top:6px solid}
.feature.about{border-color:var(--blue)}
.feature.care{border-color:var(--pink)}
.feature.community{border-color:var(--purple)}
.feature h2{font-family:'Exo 2',Arial,sans-serif;font-weight:300;font-size:26px;line-height:30px;color:#111;margin-top:22px}
.feature p{font-size:11px;line-height:17.4px;color:var(--body);margin-top:13px;padding:0 12px}
.feature-photo{height:165px;margin-top:22px}
.about .feature-photo{background:linear-gradient(120deg,#e8a060,#d9c8b0 50%,#c75a3a)}
.care .feature-photo{background:linear-gradient(120deg,#cdb9a6,#e7ddd3 50%,#3a3f5c)}
.community .feature-photo{background:linear-gradient(120deg,#8a7a6a,#a36fa8 50%,#b9a285)}

.site-footer{position:absolute;top:1014px;left:0;width:989px;height:186px;background:var(--green);color:#fff}
.footer-brand{position:absolute;left:47px;top:46px;display:flex;align-items:center;gap:10px}
.footer-brand .brand-dot{width:46px;height:46px;background:#fff}
.footer-brand .brand-name{color:#fff;font-size:18px;line-height:20px;width:180px}
.copyright{position:absolute;left:47px;top:148px;font-size:9.5px;letter-spacing:.2px}
.divider{position:absolute;top:44px;width:1px;height:115px;background:rgba(255,255,255,.6)}
.divider.one{left:358px}.divider.two{left:691px}
.footer-heading{font-family:'Exo 2',Arial,sans-serif;font-weight:400;font-size:17px;letter-spacing:.2px}
.contact{position:absolute;left:431px;top:42px}
.contact ul{list-style:none;margin-top:14px;font-size:11px;line-height:14.5px}
.contact li{display:flex;gap:10px;align-items:flex-start}
.contact li svg{flex:none;margin-top:2px}
.contact li.gap{margin-top:14px}
.social{position:absolute;left:769px;top:42px}
.social .social-row{margin-top:14px;gap:6px}
</style>
</head>
<body>

<header class="brand">
  <span class="brand-dot"></span>
  <span class="brand-name">Tarvos Neighbourhood Learning Centre</span>
</header>

<nav class="main-nav">
  <a class="active nav-green">HOME</a>
  <a class="nav-orange">COURSES</a>
  <a class="nav-blue">SOCIAL ENTERPRISE</a>
  <a class="nav-pink">COMMUNITY PROGRAMS</a>
  <a class="nav-purple">TARVOS CARES</a>
  <a class="nav-green">VENUE HIRE</a>
  <a class="nav-orange">OPENSEAT CAFÉ</a>
</nav>

<section class="hero">
  <div class="hero-slide" role="img" aria-label="Photo of several hands of different skin tones laid on a wooden table">
    <svg class="slide-arrow prev" width="14" height="22" viewBox="0 0 14 22"><path d="M11 2 L3 11 L11 20" fill="none" stroke="rgba(255,255,255,.7)" stroke-width="3"/></svg>
    <svg class="slide-arrow next" width="14" height="22" viewBox="0 0 14 22"><path d="M3 2 L11 11 L3 20" fill="none" stroke="rgba(255,255,255,.7)" stroke-width="3"/></svg>
    <div class="slide-caption">
      <h2>Hands</h2>
      <p>Our accredited Childcare and Kinder allows your child to grown in a fun learning environment, while you attend courses or activities</p>
    </div>
  </div>
  <aside class="newsletter">
    <h3>SUBSCRIBE FOR OUR <strong>NEWSLETTER</strong></h3>
    <span class="email-field">Enter your email ...</span>
    <span class="subscribe-btn">SUBSCRIBE</span>
    <div class="social-row" aria-label="Social media links">
      <span class="sq1"></span><span class="sq2"></span><span class="sq3"></span><span class="sq4"></span>
    </div>
  </aside>
</section>

<section class="features">
  <article class="feature about">
    <h2>About Us</h2>
    <p>Lorem ipsum dolor sit amet, consectetur adipiscing elit, sed do eiusmod tempor incididunt ut labore et dolore magna aliqua. Ut enim ad minim veniam, quis nostrud exercitation ullamco laboris nisi ut aliquip ex ea commodo consequat.</p>
    <div class="feature-photo" role="img" aria-label="Photo of children drawing together at a classroom table"></div>
  </article>
  <article class="feature care">
    <h2>Child Care</h2>
    <p>Lorem ipsum dolor sit amet, consectetur adipiscing elit, sed do eiusmod tempor incididunt ut labore et dolore magna aliqua. Ut enim ad minim veniam, quis nostrud exercitation ullamco laboris nisi ut aliquip ex ea commodo consequat.</p>
    <div class="feature-photo" role="img" aria-label="Photo of a carer playing with a young child and toy blocks"></div>
  </article>
  <article class="feature community">
    <h2>Our Community</h2>
    <p>Lorem ipsum dolor sit amet, consectetur adipiscing elit, sed do eiusmod tempor incididunt ut labore et dolore magna aliqua. Ut enim ad minim veniam, quis nostrud exercitation ullamco laboris nisi ut aliquip ex ea commodo consequat.</p>
    <div class="feature-photo" role="img" aria-label="Photo of older adults in an exercise class raising their arms"></div>
  </article>
</section>

<footer class="site-footer">
  <div class="footer-brand">
    <span class="brand-dot"></span>
    <span class="brand-name">Tarvos Neighbourhood Learning Centre</span>
  </div>
  <p class="copyright">COPYRIGHT © 2019 &nbsp;I&nbsp; ALL RIGHT RESERVED.</p>
  <span class="divider one"></span>
  <span class="divider two"></span>

  <div class="contact">
    <h4 class="footer-heading">TARVOS NEIGHBOURHOOD</h4>
    <ul>
      <li>
        <svg width="12" height="14" viewBox="0 0 12 14"><path d="M6 1a4 4 0 0 1 4 4c0 3-4 8-4 8S2 8 2 5a4 4 0 0 1 4-4z" fill="none" stroke="#fff" stroke-width="1.4"/><circle cx="6" cy="5" r="1.4" fill="#fff"/></svg>
        <span>47 Fenwick Road<br>Ashvale VIC 3190</span>
      </li>
      <li class="gap">
        <svg width="12" height="12" viewBox="0 0 12 12"><path d="M2 1l2.5 0 1 3-1.5 1a7 7 0 0 0 3 3l1-1.5 3 1V10a1 1 0 0 1-1 1C5 11 1 7 1 2a1 1 0 0 1 1-1z" fill="#fff"/></svg>
        <span>03 9000 4172</span>
      </li>
      <li>
        <svg width="12" height="10" viewBox="0 0 12 10"><rect x="1" y="1" width="10" height="8" fill="none" stroke="#fff" stroke-width="1.2"/><path d="M1 1l5 4 5-4" fill="none" stroke="#fff" stroke-width="1.2"/></svg>
        <span>hello@tarvoshub.org.au</span>
      </li>
    </ul>
  </div>

  <div class="social">
    <h4 class="footer-heading">SOCIAL MEDIA</h4>
    <div class="social-row" aria-label="Social media links">
      <span class="sq1"></span><span class="sq2"></span><span class="sq3"></span><span class="sq4"></span>
    </div>
  </div>
</footer>

</body>
</html>
```